Safety Work Area Signage to keep people away from work zone

We would like to create a simple design that will include our logo and phone number, 'work area', and 'caution / cuidado' (please see a mock-up of the intended design in the uploaded files). Please provide multiple options. We would like a Professional look for the poster as it is meant for safety. Poster Size to be: 18.16" X 23.10"

Target Market(s)

General Public on Construction Sites

Font styles to use
Serif

Requirements
Must have
• see mock-ups in uploaded files
Nice to have
• Simple Design, Professional Look

```html
<!DOCTYPE html>
<html lang="en">
<head>
<meta charset="utf-8">
<title>Work Area Safety Signage</title>
<link href="https://fonts.googleapis.com/css2?family=Archivo+Black&family=Merriweather:wght@700&display=swap" rel="stylesheet">
<style>
  :root {
    --navy: #2c3485;
    --red: #ee3439;
    --red-soft: #f47a7d;
    --white: #ffffff;
    --edge: #444444;
    --shadow: rgba(0, 0, 0, 0.35);
  }
  html, body {
    margin: 0;
    padding: 0;
    width: 1200px;
    height: 994px;
    overflow: hidden;
    background: var(--white);
  }
  .sign {
    position: absolute;
    top: 45px;
    width: 529px;
    height: 672px;
    filter: drop-shadow(7px 8px 6px var(--shadow));
  }
  .sign--light { left: 50px; }
  .sign--dark { left: 626px; }
  .banner {
    position: absolute;
    left: 0;
    top: 781px;
    width: 1200px;
    height: 213px;
  }
  .headline {
    font-family: "Archivo Black", "Arial Black", sans-serif;
  }
  .wordmark, .trade {
    font-family: "Merriweather", Georgia, serif;
    font-weight: 700;
  }
  .phone {
    font-family: "Archivo Black", "Arial Black", sans-serif;
    letter-spacing: 3px;
  }
</style>
</head>
<body>

<!-- Option 1: white sign -->
<svg class="sign sign--light" viewBox="0 0 529 672" role="img" aria-label="Caution work area sign, white version">
  <defs>
    <linearGradient id="hazard-light" x1="0" x2="1" y1="0" y2="0">
      <stop offset="0" stop-color="var(--red)"/>
      <stop offset="0.5" stop-color="var(--red-soft)"/>
      <stop offset="1" stop-color="var(--red)"/>
    </linearGradient>
  </defs>
  <rect class="sign-face" width="529" height="672" fill="var(--white)"/>
  <rect class="hazard-band" role="img" aria-label="Red and white hazard stripe band" y="0" width="529" height="34" fill="url(#hazard-light)"/>
  <rect class="hazard-band" role="img" aria-label="Red and white hazard stripe band" y="123" width="529" height="36" fill="url(#hazard-light)"/>
  <rect class="hazard-band" role="img" aria-label="Red and white hazard stripe band" y="636" width="529" height="36" fill="url(#hazard-light)"/>

  <text class="headline caution" x="39" y="106" font-size="71" fill="var(--navy)" textLength="454" lengthAdjust="spacing">CAUTION</text>

  <g class="work-area-outline" aria-hidden="true">
    <text class="headline" x="60" y="285" font-size="104" textLength="418" lengthAdjust="spacingAndGlyphs" fill="var(--navy)" stroke="var(--navy)" stroke-width="14" stroke-linejoin="miter">WORK</text>
    <text class="headline" x="76" y="389" font-size="104" textLength="380" lengthAdjust="spacingAndGlyphs" fill="var(--navy)" stroke="var(--navy)" stroke-width="14" stroke-linejoin="miter">AREA</text>
  </g>
  <text class="headline work-area" x="60" y="285" font-size="104" textLength="418" lengthAdjust="spacingAndGlyphs" fill="var(--red)" stroke="var(--white)" stroke-width="5" stroke-linejoin="miter" paint-order="stroke">WORK</text>
  <text class="headline work-area" x="76" y="389" font-size="104" textLength="380" lengthAdjust="spacingAndGlyphs" fill="var(--red)" stroke="var(--white)" stroke-width="5" stroke-linejoin="miter" paint-order="stroke">AREA</text>

  <g class="brand-row">
    <text class="wordmark" x="250" y="470" font-size="23" text-anchor="end" fill="var(--navy)">Hartley &amp; Co.</text>
    <line x1="261" y1="432" x2="261" y2="483" stroke="var(--navy)" stroke-width="1.5"/>
    <text class="trade" x="341" y="459" font-size="20" text-anchor="middle" fill="var(--navy)">General</text>
    <text class="trade" x="341" y="480" font-size="20" text-anchor="middle" fill="var(--navy)">Contractors</text>
  </g>

  <rect class="phone-band" y="494" width="529" height="34" fill="var(--red)"/>
  <text class="phone" x="264.5" y="520" font-size="22" text-anchor="middle" fill="var(--white)">(555) 240-0176</text>

  <text class="headline cuidado" x="43" y="607" font-size="71" fill="var(--navy)" textLength="448" lengthAdjust="spacing">CUIDADO</text>
  <rect class="sign-edge" x="0.5" y="0.5" width="528" height="671" fill="none" stroke="var(--edge)" stroke-width="1"/>
</svg>

<!-- Option 2: navy sign -->
<svg class="sign sign--dark" viewBox="0 0 529 672" role="img" aria-label="Caution work area sign, navy version">
  <defs>
    <linearGradient id="hazard-dark" x1="0" x2="1" y1="0" y2="0">
      <stop offset="0" stop-color="var(--red)"/>
      <stop offset="0.5" stop-color="#b8344a"/>
      <stop offset="1" stop-color="var(--red)"/>
    </linearGradient>
  </defs>
  <rect class="sign-face" width="529" height="672" fill="var(--navy)"/>
  <rect class="hazard-band" role="img" aria-label="Red and navy hazard stripe band" y="0" width="529" height="34" fill="url(#hazard-dark)"/>
  <rect class="hazard-band" role="img" aria-label="Red and navy hazard stripe band" y="123" width="529" height="36" fill="url(#hazard-dark)"/>
  <rect class="hazard-band" role="img" aria-label="Red and navy hazard stripe band" y="636" width="529" height="36" fill="url(#hazard-dark)"/>

  <text class="headline caution" x="39" y="106" font-size="71" fill="var(--white)" textLength="454" lengthAdjust="spacing">CAUTION</text>

  <text class="headline work-area" x="60" y="285" font-size="104" textLength="418" lengthAdjust="spacingAndGlyphs" fill="var(--red)" stroke="var(--white)" stroke-width="9" stroke-linejoin="miter" paint-order="stroke">WORK</text>
  <text class="headline work-area" x="76" y="389" font-size="104" textLength="380" lengthAdjust="spacingAndGlyphs" fill="var(--red)" stroke="var(--white)" stroke-width="9" stroke-linejoin="miter" paint-order="stroke">AREA</text>

  <g class="brand-row">
    <text class="wordmark" x="250" y="466" font-size="23" text-anchor="end" fill="var(--white)">Hartley &amp; Co.</text>
    <line x1="261" y1="428" x2="261" y2="479" stroke="var(--white)" stroke-width="1.5"/>
    <text class="trade" x="341" y="455" font-size="20" text-anchor="middle" fill="var(--white)">General</text>
    <text class="trade" x="341" y="476" font-size="20" text-anchor="middle" fill="var(--white)">Contractors</text>
  </g>

  <rect class="phone-band" y="494" width="529" height="34" fill="var(--red)"/>
  <text class="phone" x="264.5" y="520" font-size="22" text-anchor="middle" fill="var(--white)">(555) 240-0176</text>

  <text class="headline cuidado" x="43" y="607" font-size="71" fill="var(--white)" textLength="448" lengthAdjust="spacing">CUIDADO</text>
  <rect class="sign-edge" x="0.5" y="0.5" width="528" height="671" fill="none" stroke="var(--edge)" stroke-width="1"/>
</svg>

<!-- Option 3: barrier banner -->
<svg class="banner" viewBox="0 0 1200 213" role="img" aria-label="Work site barrier banner">
  <defs>
    <linearGradient id="hazard-banner" x1="0" x2="1" y1="0" y2="0">
      <stop offset="0" stop-color="var(--red-soft)"/>
      <stop offset="0.5" stop-color="#f6a3a5"/>
      <stop offset="1" stop-color="var(--red-soft)"/>
    </linearGradient>
  </defs>
  <rect class="banner-field" width="1200" height="213" fill="var(--red)"/>
  <rect class="hazard-band" role="img" aria-label="Red and white hazard stripe band" y="0" width="1200" height="38" fill="url(#hazard-banner)"/>
  <rect class="hazard-band" role="img" aria-label="Red and white hazard stripe band" y="174" width="1200" height="39" fill="url(#hazard-banner)"/>
  <rect class="phone-band" x="455" y="174" width="290" height="39" fill="var(--red)"/>

  <g class="brand-row">
    <text class="wordmark" x="575" y="126" font-size="42" text-anchor="end" fill="var(--white)">Hartley &amp; Co.</text>
    <line x1="596" y1="76" x2="596" y2="150" stroke="var(--white)" stroke-width="2"/>
    <text class="trade" x="735" y="109" font-size="37" text-anchor="middle" fill="var(--white)">General</text>
    <text class="trade" x="735" y="144" font-size="37" text-anchor="middle" fill="var(--white)">Contractors</text>
  </g>

  <text class="phone" x="600" y="204" font-size="26" text-anchor="middle" fill="var(--white)">(555) 240-0176</text>
</svg>

</body>
</html>
```